Business Card front and back

I am looking for business card design. I really really like the design file I uploaded named 627788_19250069_3478263_85f427ee_image

Target Market(s)

Corporate Fitness High end Private country club

Industry/Entity Type

Fitness Industry

Contact Information for Business Card

The last image I like as an example I uploaded a bunch of my logos. The file labeled "the signature" is my business card information for you to use

Colors
0054AA
0677BA
7BADD7
CADEEF
E8F1F8

Requirements
Must have
• E-mail sigThe file I uploaded labeled "627788_19250069_3478263_85f427ee_image" with all the plus signs on the back if those could be the logo symbol I uploaded labeled "1 back.png"

```html
<!DOCTYPE html>
<html lang="en">
<head>
<meta charset="utf-8">
<title>Stride Coaching — Business Card</title>
<link href="https://fonts.googleapis.com/css2?family=Lato:wght@400;700;900&display=swap" rel="stylesheet">
<style>
  :root {
    --page-bg: #1a1a1a;
    --card-bg: #2f2f2f;
    --mark-dark: #121212;
    --mark-mid: #3c3b3c;
    --brand-blue: #4a80c8;
    --text-light: #f2f2f2;
    --card-shadow: rgba(0, 0, 0, 0.55);
  }
  * { margin: 0; padding: 0; box-sizing: border-box; }
  html, body {
    width: 1200px;
    height: 1122px;
    overflow: hidden;
    background: var(--page-bg);
    font-family: "Lato", sans-serif;
  }
  .card {
    position: absolute;
    width: 630px;
    height: 360px;
    background: var(--card-bg);
    border-radius: 22px;
    box-shadow: 0 18px 40px var(--card-shadow);
    overflow: hidden;
  }
  .card--front { left: 480px; top: 110px; }
  .card--back { left: 90px; top: 620px; }

  .brand {
    position: absolute;
    inset: 0;
    display: flex;
    align-items: center;
    justify-content: center;
    gap: 16px;
  }
  .brand__mark {
    width: 34px;
    height: 34px;
    background: var(--brand-blue);
  }
  .brand__name {
    font-weight: 900;
    font-size: 40px;
    letter-spacing: 2px;
    color: var(--brand-blue);
    text-transform: uppercase;
  }

  .emblem-area {
    position: absolute;
    left: 36px;
    top: 34px;
    width: 292px;
    height: 292px;
    border-radius: 12px;
    background: linear-gradient(135deg, var(--mark-dark) 0%, #1c1b1c 50%, var(--mark-mid) 100%);
  }

  .contact {
    position: absolute;
    right: 36px;
    bottom: 28px;
    text-align: right;
    color: var(--text-light);
  }
  .contact__name {
    font-weight: 700;
    font-size: 30px;
    color: var(--brand-blue);
    text-transform: uppercase;
    letter-spacing: 0.5px;
    line-height: 1.05;
  }
  .contact__role {
    font-size: 19px;
    margin-bottom: 10px;
  }
  .contact__list { list-style: none; }
  .contact__item {
    display: flex;
    justify-content: flex-end;
    align-items: center;
    gap: 10px;
    font-size: 15px;
    line-height: 24px;
  }
  .contact__item--phone { font-weight: 700; font-size: 18px; }
  .contact__icon { width: 15px; height: 15px; fill: var(--brand-blue); flex: none; }
</style>
</head>
<body>
  <section class="card card--front" aria-label="Card front">
    <div class="brand">
      <span class="brand__mark"></span>
      <span class="brand__name">Stride Coaching</span>
    </div>
  </section>

  <section class="card card--back" aria-label="Card back">
    <div class="emblem-area" role="img" aria-label="Large dark brand emblem decoration"></div>
    <div class="contact">
      <p class="contact__name">Dale Marrow</p>
      <p class="contact__role">Consultant</p>
      <ul class="contact__list">
        <li class="contact__item contact__item--phone">555-014-2273
          <svg class="contact__icon" viewBox="0 0 16 16"><path d="M3.5 1 6 3.5 4.7 5.6c.8 2 2.6 3.8 4.7 4.7L11.5 9 14 11.5 12.4 14C6.5 14 2 9.5 2 3.6Z"/></svg>
        </li>
        <li class="contact__item">dale@stridecoaching.co
          <svg class="contact__icon" viewBox="0 0 16 16"><path d="M1 3h14v10H1Zm1.5 1.2L8 8.5l5.5-4.3Z"/></svg>
        </li>
        <li class="contact__item">stridecoaching.co
          <svg class="contact__icon" viewBox="0 0 16 16"><path d="M8 1a7 7 0 1 0 0 14A7 7 0 0 0 8 1Zm0 1.6a5.4 5.4 0 0 1 4.4 2.3H10L8.7 6.5 6.5 6 5 8l1.7 2.2-.5 2.8A5.4 5.4 0 0 1 3.6 4.7l1.6 1.1L7 4Z"/></svg>
        </li>
        <li class="contact__item">CO. UT. WY. MT. ID. NV
          <svg class="contact__icon" viewBox="0 0 16 16"><path d="M8 1a5 5 0 0 0-5 5c0 3.6 5 9 5 9s5-5.4 5-9a5 5 0 0 0-5-5Zm0 7a2 2 0 1 1 0-4 2 2 0 0 1 0 4Z"/></svg>
        </li>
      </ul>
    </div>
  </section>
</body>
</html>
```